Business Card Design

We need a business card design for a Dry cleaners in Brisbane, Australia. We are trying to promote a fresh/clean image consistent with our website. www.finchlanelaundry.com.au

Looking for a professional neat card that's easy to read.

Target Market(s)

Customers looking for a professional, fresh and clean drycleaners.

Industry/Entity Type

Business

Contact Information for Business Card

See our existing business card. The Fax number (07) 3648 2051 to be removed.

Requirements
Must have
• All the details on current business card less the fax number.
Nice to have
• I like white text on coloured background. Blue works well as we are located near the water...

```html
<!DOCTYPE html>
<html lang="en">
<head>
<meta charset="utf-8">
<title>Finch Lane Laundry – Business Card</title>
<link rel="stylesheet" href="https://fonts.googleapis.com/css2?family=Source+Sans+3:wght@400;600;700&display=swap">
<style>
  :root {
    --backdrop: #3a3a3a;
    --card-white: #ffffff;
    --brand-blue: #2f48a0;
    --sky-blue: #27a9e1;
    --ink: #111111;
    --on-blue: #ffffff;
  }
  html, body {
    margin: 0;
    padding: 0;
    width: 1200px;
    height: 999px;
    overflow: hidden;
    background: var(--backdrop);
    font-family: "Source Sans 3", "Myriad Pro", Arial, sans-serif;
  }
  .card {
    position: absolute;
    left: 75px;
    top: 199px;
    width: 1050px;
    height: 600px;
    background: var(--card-white);
    overflow: hidden;
  }
  .card-wave {
    position: absolute;
    inset: 0;
    width: 1050px;
    height: 600px;
  }
  .brand-name {
    position: absolute;
    top: 130px;
    left: 0;
    width: 100%;
    text-align: center;
    font-size: 72px;
    font-weight: 700;
    color: var(--brand-blue);
    letter-spacing: 1px;
    margin: 0;
    line-height: 1;
  }
  .branch-list {
    position: absolute;
    top: 302px;
    left: 0;
    width: 100%;
    display: flex;
    justify-content: center;
    align-items: center;
    gap: 34px;
    font-size: 37px;
    color: var(--ink);
    margin: 0;
    padding: 0;
    list-style: none;
    line-height: 1;
  }
  .contact-column {
    position: absolute;
    top: 408px;
    color: var(--on-blue);
  }
  .contact-address {
    position: relative;
    padding-left: 35px;
    font-size: 27px;
    line-height: 34px;
    font-style: normal;
  }
  .contact-address .line-small { font-size: 24px; }
  .contact-phone {
    position: relative;
    margin-top: 16px;
    padding-left: 38px;
    font-size: 28px;
    line-height: 34px;
  }
  .icon {
    position: absolute;
    left: 0;
    top: 4px;
    fill: var(--on-blue);
  }
  .col-one { left: 45px; }
  .col-two { left: 345px; }
  .col-three { left: 673px; }
  .website {
    position: absolute;
    top: 543px;
    left: 0;
    width: 100%;
    text-align: center;
    font-size: 27px;
    color: var(--on-blue);
  }
</style>
</head>
<body>
  <main class="card">
    <svg class="card-wave" viewBox="0 0 1050 600" aria-hidden="true">
      <path d="M420 392 Q 760 380 1050 324 L1050 420 L420 420 Z" fill="var(--sky-blue)"/>
      <path d="M0 354 Q 480 430 1050 366" fill="none" stroke="var(--card-white)" stroke-width="6"/>
      <path d="M0 354 Q 480 430 1050 366 L1050 600 L0 600 Z" fill="var(--brand-blue)"/>
    </svg>

    <h1 class="brand-name">Finch Lane Laundry</h1>

    <ul class="branch-list">
      <li>Wynnum</li>
      <li class="divider">|</li>
      <li>Cleveland</li>
      <li class="divider">|</li>
      <li>Victoria Pt</li>
    </ul>

    <section class="contact-column col-one">
      <address class="contact-address">
        <svg class="icon" width="20" height="28" viewBox="0 0 20 28"><path d="M10 0C4.5 0 0 4.4 0 9.8 0 17 10 28 10 28s10-11 10-18.2C20 4.4 15.5 0 10 0zm0 14a4.3 4.3 0 1 1 0-8.6A4.3 4.3 0 0 1 10 14z"/></svg>
        18 Marlow Rd<br>Wynnum Qld 4100
      </address>
      <div class="contact-phone">
        <svg class="icon" width="24" height="24" viewBox="0 0 24 24"><path d="M6.6 2.5l3 3.6-2 2.2c1.2 2.8 3.3 4.9 6.1 6.1l2.2-2 3.6 3-1.8 3.4C10 18.4 5.6 14 2.8 6.1z"/><path d="M14 3a7 7 0 0 1 7 7" stroke="#fff" stroke-width="2" fill="none"/><path d="M14 7a3 3 0 0 1 3 3" stroke="#fff" stroke-width="2" fill="none"/></svg>
        (07) 3274 6190
      </div>
    </section>

    <section class="contact-column col-two">
      <address class="contact-address">
        <svg class="icon" width="20" height="28" viewBox="0 0 20 28"><path d="M10 0C4.5 0 0 4.4 0 9.8 0 17 10 28 10 28s10-11 10-18.2C20 4.4 15.5 0 10 0zm0 14a4.3 4.3 0 1 1 0-8.6A4.3 4.3 0 0 1 10 14z"/></svg>
        <span class="line-small">Shop 3/41 Hartley St</span><br>Cleveland
      </address>
      <div class="contact-phone">
        <svg class="icon" width="24" height="24" viewBox="0 0 24 24"><path d="M6.6 2.5l3 3.6-2 2.2c1.2 2.8 3.3 4.9 6.1 6.1l2.2-2 3.6 3-1.8 3.4C10 18.4 5.6 14 2.8 6.1z"/><path d="M14 3a7 7 0 0 1 7 7" stroke="#fff" stroke-width="2" fill="none"/><path d="M14 7a3 3 0 0 1 3 3" stroke="#fff" stroke-width="2" fill="none"/></svg>
        (07) 315422 7093
      </div>
    </section>

    <section class="contact-column col-three">
      <address class="contact-address">
        <svg class="icon" width="20" height="28" viewBox="0 0 20 28"><path d="M10 0C4.5 0 0 4.4 0 9.8 0 17 10 28 10 28s10-11 10-18.2C20 4.4 15.5 0 10 0zm0 14a4.3 4.3 0 1 1 0-8.6A4.3 4.3 0 0 1 10 14z"/></svg>
        <span class="line-small">Harbourside Shopping Centre</span><br>Victoria Pt
      </address>
      <div class="contact-phone">
        <svg class="icon" width="24" height="24" viewBox="0 0 24 24"><path d="M6.6 2.5l3 3.6-2 2.2c1.2 2.8 3.3 4.9 6.1 6.1l2.2-2 3.6 3-1.8 3.4C10 18.4 5.6 14 2.8 6.1z"/><path d="M14 3a7 7 0 0 1 7 7" stroke="#fff" stroke-width="2" fill="none"/><path d="M14 7a3 3 0 0 1 3 3" stroke="#fff" stroke-width="2" fill="none"/></svg>
        (07) 3521 8460
      </div>
    </section>

    <div class="website">www.finchlanelaundry.com.au</div>
  </main>
</body>
</html>
```